BrickPlayo Business Card

We need a business card design for our company. We sell construction-themed amusement rides for kids.

Contact Information for Business Card

Contact info on business card should include:
Lars Wendt
Co-Founder & COO
(833) 527-BRIKPLA
Lars@brickplayo.com
www.brickplayo.com

```html
<!DOCTYPE html>
<html lang="en">
<head>
<meta charset="utf-8">
<title>BrickPlayo Business Card</title>
<link rel="stylesheet" href="https://fonts.googleapis.com/css2?family=Open+Sans:wght@400;600;700;800&display=swap">
<style>
  :root {
    --bg: #606166;
    --card: #1d1d1d;
    --accent: #e8692b;
    --text: #ffffff;
    --muted: #d6d6d6;
  }
  * { margin: 0; padding: 0; box-sizing: border-box; }
  html, body { width: 1200px; height: 811px; overflow: hidden; }
  body {
    background: var(--bg);
    font-family: "Open Sans", Arial, sans-serif;
    display: flex;
    align-items: center;
    justify-content: center;
    gap: 40px;
  }
  .card {
    width: 540px;
    height: 309px;
    background: var(--card);
    position: relative;
    box-shadow: 0 10px 30px rgba(0,0,0,.35);
  }
  .brand {
    display: flex;
    align-items: center;
    gap: 10px;
    color: var(--accent);
    font-weight: 800;
    font-size: 34px;
    letter-spacing: .5px;
  }
  .brand-dot {
    width: 14px; height: 14px;
    border-radius: 50%;
    background: var(--accent);
  }
  .card-front {
    display: flex;
    align-items: center;
    justify-content: center;
  }
  .card-front .brand { font-size: 42px; }
  .card-back .brand {
    position: absolute;
    left: 32px;
    top: 50%;
    transform: translateY(-50%);
    font-size: 30px;
  }
  .divider {
    position: absolute;
    left: 268px;
    top: 26px;
    bottom: 26px;
    width: 1px;
    background: linear-gradient(to bottom, rgba(232,105,43,0), var(--accent) 20%, var(--accent) 80%, rgba(232,105,43,0));
  }
  .details {
    position: absolute;
    left: 300px;
    top: 52px;
    color: var(--text);
  }
  .name { font-size: 19px; font-weight: 700; line-height: 1.2; }
  .role { font-size: 12px; color: var(--muted); margin-top: 2px; }
  .contact { list-style: none; margin-top: 38px; }
  .contact li {
    display: flex;
    align-items: center;
    gap: 9px;
    font-size: 11.5px;
    line-height: 1;
    margin-bottom: 9px;
    color: var(--text);
  }
  .contact svg { width: 11px; height: 11px; flex: none; }
</style>
</head>
<body>
  <div class="card card-front">
    <div class="brand"><span class="brand-dot"></span>BrickPlayo</div>
  </div>

  <div class="card card-back">
    <div class="brand"><span class="brand-dot"></span>BrickPlayo</div>
    <div class="divider"></div>
    <div class="details">
      <div class="name">Lars Wendt</div>
      <div class="role">Co-Founder &amp; COO</div>
      <ul class="contact">
        <li>
          <svg viewBox="0 0 12 12" aria-hidden="true"><rect x="3" y="0.5" width="6" height="11" rx="1" fill="none" stroke="#e8692b" stroke-width="1.3"/><circle cx="6" cy="9.5" r=".8" fill="#e8692b"/></svg>
          (833) 527-BRIKPLA
        </li>
        <li>
          <svg viewBox="0 0 12 12" aria-hidden="true"><rect x="0.5" y="2.5" width="11" height="7" fill="#e8692b"/><path d="M0.5 2.5 6 7 11.5 2.5" fill="none" stroke="#1d1d1d" stroke-width="1"/></svg>
          Lars@brickplayo.com
        </li>
        <li>
          <svg viewBox="0 0 12 12" aria-hidden="true"><circle cx="6" cy="6" r="5.5" fill="#e8692b"/><path d="M0.5 6h11M6 .5c-2.5 3-2.5 8 0 11M6 .5c2.5 3 2.5 8 0 11" fill="none" stroke="#1d1d1d" stroke-width=".8"/></svg>
          www.brickplayo.com
        </li>
      </ul>
    </div>
  </div>
</body>
</html>
```